Marketing One-Sheet for Security Deposit Claim Notice

I need a one-sheet flyer formatted for email distribution — optimized as a JPEG/PNG that I can insert into Constant Contact or Outlook. I do not want to attach it to an email, but insert it in the email we send out. I would like it to look professional but engaging. Some images would be good, but want to make sure it reads well if images do not load for the recipients. The text is in the attached Word document, but I am open to changes/ideas that may be better for marketing purposes. I included the URLs for some of the links I would like in the one-sheet that is clickable. The logo for the business is being uploaded on the Word document. Proposed text is also uploaded in a Word document. Thank you.

Target Market(s)

Landlords, Real Estate Agents, Property Managers

Industry/Entity Type

Legal

Requirements
Must have
• Professional but appealing design. The One-sheet is going to be placed in the body of emails, not as an attachment.
Nice to have
• Include our logo for the business and the web links please.
Should not have
• Images can be ok, but it needs to look right if images do not download from the email sent out.

```html
<!DOCTYPE html>
<html lang="en">
<head>
<meta charset="utf-8">
<title>Security Deposit Claim Notice</title>
<link href="https://fonts.googleapis.com/css2?family=PT+Serif:ital,wght@0,400;0,700;1,400;1,700&display=swap" rel="stylesheet">
<style>
:root{
  --red:#b0101e;
  --red-bright:#e01020;
  --red-deep:#a20f1b;
  --ink:#1e1e1e;
  --muted:#555;
  --line:#c9c9c9;
  --bar:#161616;
  --white:#fff;
}
*{margin:0;padding:0;box-sizing:border-box}
html,body{width:1200px;height:2998px;overflow:hidden;background:var(--white)}
body{font-family:"PT Serif",Georgia,serif;color:var(--ink);position:relative}
.abs{position:absolute}

/* header */
.site-header{left:0;top:0;width:1200px;height:172px;background:var(--white)}
.brand-name{left:150px;top:52px;font-size:34px;font-weight:700;color:var(--red);line-height:1.1;width:300px}
.contact-band{right:0;top:0;width:636px;height:172px;background:linear-gradient(100deg,var(--red-bright),var(--red-deep));clip-path:polygon(112px 0,100% 0,100% 100%,0 100%)}
.contact-row{display:flex;align-items:center;color:var(--white);font-weight:700;white-space:nowrap}
.contact-row.phone{left:640px;top:20px;font-size:40px;font-style:italic}
.contact-row.web{left:582px;top:90px;font-size:40px}
.ico-circle{width:66px;height:66px;border-radius:50%;background:var(--white);display:flex;align-items:center;justify-content:center;margin-right:36px;box-shadow:0 0 0 6px rgba(255,255,255,.35);flex:none}

/* hero */
.hero{left:0;top:172px;width:1200px;height:575px;background:linear-gradient(90deg,#3c3028 0%,#5a4535 45%,#7a5a40 70%,#2a211c 100%)}
.hero-title{left:45px;top:390px;font-size:58px;font-weight:700;font-style:italic;color:var(--white);line-height:76px;letter-spacing:.5px}

/* benefits */
.section-title{width:1200px;text-align:center;font-size:38px;color:var(--ink);letter-spacing:.3px}
.section-title b{color:var(--red)}
.benefit{top:930px;width:314px;height:224px;border:3px solid var(--line);border-radius:6px;text-align:center;font-size:25px;line-height:33px;padding-top:124px}
.benefit .badge{position:absolute;left:50%;top:24px;transform:translateX(-50%);width:72px;height:72px;border-radius:50%;background:var(--red);display:flex;align-items:center;justify-content:center}

/* fee banner */
.fee-banner{left:45px;top:1238px;width:1110px;height:310px;border-radius:16px;background:linear-gradient(90deg,#b51b2a,#c23342 50%,#b51b2a);color:var(--white);text-align:center}
.fee-banner h2{margin-top:82px;font-size:37px;font-weight:700;letter-spacing:.3px}
.fee-banner p{margin-top:18px;font-size:36px;font-weight:700}
.fee-banner p span{font-size:68px;vertical-align:-4px}

/* florida law */
.law-title{left:44px;top:1632px;font-size:38px;line-height:48px}
.law-title b{color:var(--red)}
.law-intro{left:45px;top:1742px;font-size:23px;line-height:31px;width:570px}
.law-list{left:44px;top:1836px;list-style:none;font-size:19px;color:#333}
.law-list li{display:flex;align-items:center;height:52px}
.law-list .arrow{width:22px;height:22px;border-radius:50%;background:var(--red-bright);margin-right:22px;display:flex;align-items:center;justify-content:center}
.team-photo{left:716px;top:1625px;width:439px;height:343px;border-radius:8px;background:linear-gradient(120deg,#d8dde3,#eef1f4 55%,#b7c2cc)}
.law-note{left:45px;top:2030px;width:1110px;font-size:21px;line-height:38px;color:#444}

/* commercial */
.commercial{left:44px;top:2229px;width:1111px;height:437px;border-radius:10px;overflow:hidden;background:linear-gradient(135deg,var(--red-bright),var(--red-deep))}
.commercial-photo{position:absolute;left:0;top:0;width:560px;height:437px;background:linear-gradient(130deg,#4a4a4a,#9a9a9a 50%,#d8d8d8);clip-path:polygon(0 0,440px 0,530px 230px,440px 437px,0 437px)}
.commercial-edge{position:absolute;left:0;top:0}
.commercial h2{position:absolute;left:590px;top:48px;width:480px;font-size:38px;line-height:52px;color:var(--white);font-weight:700}
.btn-light{position:absolute;background:var(--white);color:var(--ink);font-weight:700;font-size:15px;border-radius:4px}
.btn-contact{left:589px;top:228px;padding:15px 22px}
.btn-hire{left:587px;top:296px;width:490px;padding:14px 16px;line-height:22px}

/* footer */
.foot-name{left:38px;top:2764px;font-size:33px;color:var(--red);white-space:nowrap}
.foot-contact{display:flex;align-items:center;font-size:23px;white-space:nowrap}
.foot-contact .ico-circle{width:46px;height:46px;background:var(--red-bright);margin-right:14px;box-shadow:none}
.foot-sep{left:778px;top:2760px;width:2px;height:40px;background:var(--ink)}
.btn-red{top:2840px;height:53px;border-radius:5px;background:var(--red-bright);color:var(--white);font-size:27px;display:flex;align-items:center;justify-content:center}
.copyright{left:0;top:2944px;width:1200px;height:54px;background:var(--bar);color:var(--white);font-size:16px;font-weight:700;padding:20px 48px}
</style>
</head>
<body>

<header class="abs site-header">
  <div class="abs brand-name">Harbor Claim Counsel</div>
</header>
<div class="abs contact-band"></div>
<div class="abs contact-row phone">
  <span class="ico-circle"><svg width="30" height="30" viewBox="0 0 24 24"><path fill="#e01020" d="M6.6 10.8a15 15 0 006.6 6.6l2.2-2.2a1 1 0 011-.25 11.4 11.4 0 003.6.6 1 1 0 011 1V20a1 1 0 01-1 1A17 17 0 013 4a1 1 0 011-1h3.5a1 1 0 011 1c0 1.25.2 2.45.6 3.6a1 1 0 01-.25 1z"/></svg></span>
  1 (877) 555-0142
</div>
<div class="abs contact-row web">
  <span class="ico-circle"><svg width="32" height="32" viewBox="0 0 24 24"><circle cx="12" cy="12" r="11" fill="#e01020"/><rect x="6" y="8" width="12" height="8" fill="none" stroke="#fff" stroke-width="1.5"/><path d="M6 8l6 5 6-5M6 16l4-4M18 16l-4-4" fill="none" stroke="#fff" stroke-width="1.5"/></svg></span>
  HarborClaimCounsel.com
</div>

<div class="abs hero" role="img" aria-label="Photo of a model house on a desk beside a hand signing documents"></div>
<h1 class="abs hero-title">SECURITY DEPOSIT<br>CLAIM NOTICE</h1>

<h2 class="abs section-title" style="top:830px;font-weight:400">KEEP THE <b>TENANT’S SECURITY DEPOSIT</b></h2>

<div class="abs benefit" style="left:88px">
  <span class="badge"><svg width="38" height="38" viewBox="0 0 24 24"><rect x="2" y="6" width="16" height="11" fill="none" stroke="#fff" stroke-width="1.8"/><text x="10" y="15" font-size="9" font-weight="700" fill="#fff" text-anchor="middle" font-family="serif">$</text><circle cx="18" cy="16" r="4.5" fill="#fff"/><path d="M16 14l4 4M20 14l-4 4" stroke="#b0101e" stroke-width="1.6"/></svg></span>
  Cover unpaid Rent
</div>
<div class="abs benefit" style="left:450px">
  <span class="badge"><svg width="38" height="38" viewBox="0 0 24 24"><circle cx="14" cy="7" r="5" fill="none" stroke="#fff" stroke-width="1.8"/><text x="14" y="10" font-size="8" font-weight="700" fill="#fff" text-anchor="middle" font-family="serif">$</text><path d="M2 15h4l4 2h5a1.5 1.5 0 010 3H9M2 21h12l7-4" fill="none" stroke="#fff" stroke-width="1.8"/></svg></span>
  Apply to legal fees<br>and costs
</div>
<div class="abs benefit" style="left:810px">
  <span class="badge"><svg width="38" height="38" viewBox="0 0 24 24"><path d="M3 12l9-8 9 8v9H3z" fill="#fff"/><rect x="8" y="13" width="4" height="5" fill="#b0101e"/><path d="M14 8l2 4-2 3 2 4" stroke="#b0101e" stroke-width="1.6" fill="none"/></svg></span>
  Charge against Damages<br>to the Property
</div>

<section class="abs fee-banner">
  <h2>WE PREPARE SECURITY DEPOSIT CLAIM NOTICES</h2>
  <p>FLAT FEE <span>$350</span></p>
</section>

<h2 class="abs law-title" style="font-weight:400">FOLLOW FLORIDA <b>LAW TO<br>KEEP THE DEPOSIT</b></h2>
<p class="abs law-intro">If the Security Deposit Claim is not made correctly and on time, then:</p>
<ul class="abs law-list">
  <li><span class="arrow"><svg width="12" height="12" viewBox="0 0 12 12"><path d="M2 6h7M6 3l3 3-3 3" stroke="#fff" stroke-width="1.8" fill="none"/></svg></span>Tenant is automatically entitled to their full deposit back</li>
  <li><span class="arrow"><svg width="12" height="12" viewBox="0 0 12 12"><path d="M2 6h7M6 3l3 3-3 3" stroke="#fff" stroke-width="1.8" fill="none"/></svg></span>No claim against the deposit can be made</li>
  <li><span class="arrow"><svg width="12" height="12" viewBox="0 0 12 12"><path d="M2 6h7M6 3l3 3-3 3" stroke="#fff" stroke-width="1.8" fill="none"/></svg></span>Tenant can sue and recover the deposit and thousands in legal fees</li>
</ul>
<div class="abs team-photo" role="img" aria-label="Photo of two attorneys standing in a bright office"></div>
<p class="abs law-note">There are lawyers that specialize in representing tenants and go after landlords that do not make a proper claim against the security deposit. They sue and win their cases and get thousands of dollars in legal fees against Landlords, even if the tenant owes unpaid rent</p>

<section class="abs commercial">
  <div class="commercial-photo" role="img" aria-label="Photo of a model office building on a desk beside a signed contract"></div>
  <svg class="commercial-edge" width="560" height="437" viewBox="0 0 560 437"><polyline points="440,0 530,230 440,437" fill="none" stroke="#fff" stroke-width="10"/></svg>
  <h2>FOR COMMERCIAL PROPERTIES, THE FLAT LEGAL FEE IS $450</h2>
  <span class="btn-light btn-contact">CONTACT US</span>
  <span class="btn-light btn-hire">HIRE US TO PREPARE AND SERVE TO THE TENANT THE SECURITY DEPOSIT CLAIM</span>
</section>

<div class="abs foot-name">HARBOR CLAIM COUNSEL</div>
<div class="abs foot-contact" style="left:512px;top:2758px">
  <span class="ico-circle"><svg width="24" height="24" viewBox="0 0 24 24"><path fill="#fff" d="M6.6 10.8a15 15 0 006.6 6.6l2.2-2.2a1 1 0 011-.25 11.4 11.4 0 003.6.6 1 1 0 011 1V20a1 1 0 01-1 1A17 17 0 013 4a1 1 0 011-1h3.5a1 1 0 011 1c0 1.25.2 2.45.6 3.6a1 1 0 01-.25 1z"/></svg></span>
  1877-555-0142
</div>
<div class="abs foot-sep"></div>
<div class="abs foot-contact" style="left:840px;top:2754px">
  <span class="ico-circle"><svg width="24" height="24" viewBox="0 0 24 24"><rect x="4" y="6" width="16" height="12" fill="none" stroke="#fff" stroke-width="1.8"/><path d="M4 6l8 6 8-6M4 18l6-6M20 18l-6-6" fill="none" stroke="#fff" stroke-width="1.8"/></svg></span>
  HarborClaimCounsel.com
</div>
<a class="abs btn-red" style="left:45px;width:274px;text-decoration:none">More Information</a>
<a class="abs btn-red" style="left:330px;width:408px;text-decoration:none">Request our Hiring Documents</a>

<footer class="abs copyright">Copyright © 2025 Harbor Claim Counsel. All rights reserved.</footer>

</body>
</html>
```